HomePage Design for Lumen Getaways - once-in-a-lifetime experiences for busy working people

Design a homepage for the Lumen Getaways (www.lumengetaways.example) website compatible with further web pages and the design briefing documents attached

LG HomePage Design Brief
We are seeking website HomePage designs incorporating our new Logo and colour scheme, for Lumen Getaways (www.lumengetaways.example) to go with the site functionality and wireframe ideas attached.
The website HomePage design needs to
• Incorporate and be consistent with the LG Logo and its colour scheme attached.
• Express the brand values of being inspirational, high quality, upscale, cultured, aspirational, and contemporary – even somewhat ‘hip’. Probably positioned somewhere between Harlow Pike (Deluxe Travel) and Green Walrus (Hip Travel) – see https://www.harlowpike.example and https://www.greenwalrus.example .
• Be instantly recognisable and different from other travel websites and instantly communicate the nature of the brand proposition and target customer base.
• Appeal to our core 25-55 affluent businesspeople demographic
• Work in the UK, US/Canada and Australia/NZ and ultimately in mainland Europe.
• Use fonts and colours that are easily reproduced online and compatible with nearly all browsers.
• Be part of a responsive website design, that can be used both on Desktops and laptops but also with tablets and mobile ‘phones (hence content not too wide across the page)
• Feature the strapline ‘Lumen Getaways in less than 7 Days’
• Work with the and wireframes and processes shown in the attached presentation – although intended as a guide only these features and processes all need to be incorporated into the HomePage.
• Make full use of high quality images and video to convey our brand proposition and products

Target Market(s)

25-55 affluent businesspeople

Industry/Entity Type

Travel Industry

Number of Pages Required

1 page

Font styles to use
Sans Serif

Colors
0455a3
00a88f

Requirements
Must have
• • Incorporate and be consistent with the LG Logo and its colour scheme attached.
• • Express the brand values of being inspirational, high quality, upscale, cultured, aspirational, and contemporary – even somewhat ‘hip’. Probably positioned somewhere between Harlow Pike (Deluxe Travel) and Green Walrus (Hip Travel) – see https://www.harlowpike.example and https://www.greenwalrus.example .
• • Be instantly recognisable and different from other travel websites and instantly communicate the nature of the brand proposition and target customer base.
• • Appeal to our core 25-55 affluent businesspeople demographic
• • Be part of a responsive website design, that can be used both on Desktops and laptops but also with tablets and mobile ‘phones (hence content not too wide across the page)
• • Feature the strapline ‘Lumen Getaways in less than 7 Days’
• • Work with the and wireframes and processes shown in the attached presentation – although intended as a guide only these features and processes all need to be incorporated into the HomePage.
• • Make full use of high quality images and video to convey our brand proposition and products
• Colours as per Logo not as shown below
Nice to have
• • Work in the UK, US/Canada and Australia/NZ and ultimately in mainland Europe.
Should not have
• Must not be cheap or mass-market, nor excessively "stuffy or luxury-orientated"

```html
<!DOCTYPE html>
<html lang="en">
<head>
<meta charset="utf-8">
<title>Lumen Getaways – Home</title>
<link rel="stylesheet" href="https://fonts.googleapis.com/css2?family=Source+Sans+3:ital,wght@0,400;0,600;0,700;1,400&display=swap">
<style>
:root{
  --green:#1e6a34;
  --green-dark:#154f26;
  --ink:#222;
  --muted:#666;
  --line:#e3e3e3;
  --navy:#1f2d5c;
  --footer:#f3f3f3;
  --white:#fff;
}
*{box-sizing:border-box;margin:0;padding:0}
html,body{width:1200px;height:3158px;overflow:hidden}
body{position:relative;font-family:"Source Sans 3",Arial,sans-serif;color:var(--ink);background:var(--white)}
.abs{position:absolute}

/* header */
.site-header{left:0;top:0;width:1200px;height:116px}
.brand{left:112px;top:34px;display:flex;align-items:center;gap:10px}
.brand-mark{width:40px;height:40px;border-radius:50%;background:var(--green)}
.brand-name{font-size:22px;font-weight:700;color:var(--green);line-height:1}
.brand-tag{font-size:10px;color:var(--muted);letter-spacing:1px;margin-top:4px}
.social{display:flex;gap:8px}
.social span{width:28px;height:28px;border-radius:50%;border:2px solid #555;display:block}
.header-social{left:737px;top:42px}
.contact{right:112px;top:38px;text-align:right}
.contact small{font-size:13px;color:var(--muted);display:block}
.contact strong{font-size:17px;font-weight:700;letter-spacing:.5px}

.main-nav{left:0;top:116px;width:1200px;height:38px;background:var(--green);display:flex;justify-content:center;gap:48px;align-items:center}
.main-nav a{color:var(--white);text-decoration:none;font-size:14px;font-weight:600}

/* hero */
.hero{left:0;top:154px;width:1200px;height:505px;background:linear-gradient(120deg,#2c3324 0%,#4a3b2a 35%,#2b2f36 60%,#5a4630 80%,#2e3428 100%)}
.finder{left:453px;top:246px;width:299px;height:404px;background:rgba(10,10,10,.78);border:2px solid rgba(255,255,255,.15);text-align:center;padding-top:34px}
.finder-mark{width:38px;height:38px;border-radius:50%;background:var(--green);margin:0 auto}
.finder h2{color:var(--white);font-size:13px;font-weight:700;letter-spacing:.5px;margin:26px 0 22px}
.finder .field{width:230px;height:34px;margin:0 auto 10px;background:var(--white);display:flex;justify-content:space-between;align-items:center;font-size:13px;color:#555;padding-left:10px}
.finder .field i{width:30px;height:34px;background:#ddd;display:flex;align-items:center;justify-content:center}
.finder .btn{width:230px;height:36px;margin:12px auto 0;background:var(--green);color:var(--white);font-size:13px;font-weight:700;display:flex;align-items:center;justify-content:center}

/* intro */
.intro-title{left:0;top:702px;width:1200px;text-align:center;font-size:30px;font-weight:600}
.intro-title em{font-style:normal;color:var(--green)}
.intro-sub{left:0;top:742px;width:1200px;text-align:center;font-size:15px;color:var(--muted)}
.tile{width:240px;height:238px;display:flex;align-items:flex-end;justify-content:center;padding-bottom:22px;color:var(--white);font-size:14px;font-weight:700;text-align:center;line-height:1.1;text-transform:uppercase}
.faint-mark{left:890px;top:1060px;width:170px;height:170px;border-radius:50%;background:#f2f2f2}

.rule{left:0;width:1200px;height:1px;background:var(--line)}

/* videos / offers */
.h-section{font-size:26px;font-weight:600}
.video{left:112px;top:1440px;width:745px;height:436px;background:linear-gradient(180deg,#2a3140 0%,#3b3a33 45%,#5b4a35 100%)}
.play{left:447px;top:1633px;width:68px;height:46px;border-radius:10px;background:var(--white)}
.offer{left:863px;width:225px;height:139px;display:flex;flex-direction:column;align-items:center;justify-content:center;color:var(--white);font-weight:700;text-transform:uppercase;font-size:14px;text-align:center;line-height:1.2}
.offer b{font-size:20px}

/* events */
.event{top:2031px;width:308px;height:289px;border:4px solid #e6e6e6;padding:24px 26px}
.event .date{display:inline-block;background:var(--navy);color:var(--white);font-size:10px;font-weight:700;padding:3px 8px}
.event h3{font-size:17px;font-weight:700;line-height:1.2;margin:14px 0 12px}
.event p{font-size:13px;color:var(--muted);line-height:1.6}
.event .more{font-size:12px;font-style:italic;color:#999;margin-top:12px}

/* testimonial */
.count{left:112px;top:2420px;font-size:50px;font-weight:700;color:var(--green-dark)}
.count-text{left:112px;top:2478px;font-size:26px;font-weight:600;line-height:1.2}
.quote{left:446px;top:2422px;width:280px;font-size:13.5px;color:var(--muted);line-height:1.6}
.quote-foot{left:446px;top:2680px;width:290px;border-top:1px solid var(--line);padding-top:14px;display:flex;justify-content:space-between}
.sign{width:80px;height:36px;background:#f1f1f1}
.person{text-align:right;font-size:13px}
.person b{color:var(--green);display:block}
.portrait{left:779px;top:2425px;width:309px;height:312px;background:linear-gradient(135deg,#e8ddc9,#c9b49a 60%,#efe7da)}
.dots{left:913px;top:2752px;display:flex;gap:5px}
.dots span{width:10px;height:10px;border-radius:50%;background:#ccc}
.dots span:first-child{background:var(--green)}

/* footer */
.site-footer{left:0;top:2821px;width:1200px;height:337px;background:var(--footer)}
.partner{top:2846px;width:126px;height:28px;background:#d6d6d6;border-radius:14px}
.footer-rule{left:112px;top:2900px;width:976px;height:1px;background:#ddd}
.f-col{top:2926px;font-size:12.5px;color:#444;line-height:21px}
.footer-social{left:515px;top:3062px}
.copyright{left:0;top:3104px;width:1200px;text-align:center;font-size:12.5px;color:#444}
</style>
</head>
<body>

<header class="abs site-header">
  <div class="abs brand">
    <span class="brand-mark"></span>
    <div>
      <div class="brand-name">Lumen Getaways</div>
      <div class="brand-tag">IN LESS THAN 7 DAYS</div>
    </div>
  </div>
  <div class="abs social header-social"><span></span><span></span><span></span><span></span><span></span></div>
  <div class="abs contact"><small>Have Any Question? Call Us!</small><strong>000 700 2046 518</strong></div>
</header>

<nav class="abs main-nav">
  <a>Destinations</a><a>Experiences</a><a>Trips by Month</a><a>Topical Now</a><a>Tailored</a><a>Pioneers Club</a><a>Client Log-In</a><a>Blogs &amp; Reviews</a>
</nav>

<section class="abs hero" role="img" aria-label="Collage of travel photos: wildlife, festivals, balloons, mosques, climbers"></section>
<form class="abs finder">
  <div class="finder-mark"></div>
  <h2>LET'S GET STARTED</h2>
  <div class="field">What would you like to do?<i><svg width="10" height="6"><path d="M0 0h10L5 6z" fill="#555"/></svg></i></div>
  <div class="field">Where would you like to do?<i><svg width="10" height="6"><path d="M0 0h10L5 6z" fill="#555"/></svg></i></div>
  <div class="field">When do you want to travel?<i><svg width="10" height="6"><path d="M0 0h10L5 6z" fill="#555"/></svg></i></div>
  <div class="btn">TAKE ME THERE</div>
</form>

<h1 class="abs intro-title">Lumen Getaways in less than <em>7 Days!</em></h1>
<p class="abs intro-sub">Get onboard now for the launch of our brand new online platform offering once-in-a-lifetime experiences for busy people.</p>

<div class="abs tile" style="left:112px;top:796px;background:linear-gradient(160deg,#3f5a2a,#1f2a18)" role="img" aria-label="Gorilla in the forest">Wonders of Wildlife</div>
<div class="abs tile" style="left:358px;top:796px;background:linear-gradient(160deg,#c2561f,#5a2a5a)" role="img" aria-label="Carnival dancer in costume">World's Greatest<br>Festivals</div>
<div class="abs tile" style="left:604px;top:796px;background:linear-gradient(160deg,#4e6b3a,#2a3a22)" role="img" aria-label="Person on a zip line in the jungle">Must Do Activities</div>
<div class="abs tile" style="left:850px;top:796px;background:linear-gradient(160deg,#8fa0b8,#c45a2a)" role="img" aria-label="Hot air balloons in the sky">Unique Annual Events</div>
<div class="abs tile" style="left:112px;top:1044px;background:linear-gradient(160deg,#6e8fb0,#8a6a48)" role="img" aria-label="City of domes and minarets by the sea">Extraordinary &amp;<br>Secret Places</div>
<div class="abs tile" style="left:358px;top:1044px;background:linear-gradient(160deg,#6a2418,#2a0e0a)" role="img" aria-label="Tango dancers on stage">Unforgettable<br>Performances</div>
<div class="abs tile" style="left:604px;top:1044px;background:linear-gradient(160deg,#7aa0c4,#3a5878)" role="img" aria-label="Climber on an ice wall">Spectacular Hiking,<br>Climbing &amp; Walking</div>
<div class="abs faint-mark"></div>

<div class="abs rule" style="top:1332px"></div>

<h2 class="abs h-section" style="left:112px;top:1378px">Lumen Getaways Videos</h2>
<h2 class="abs h-section" style="left:893px;top:1378px">Special Offers</h2>
<div class="abs video" role="img" aria-label="Video still: photographer watching elephants at a waterhole"></div>
<div class="abs play"><svg width="68" height="46"><path d="M28 15v16l14-8z" fill="#111"/></svg></div>
<div class="abs offer" style="top:1440px;background:linear-gradient(160deg,#2a6a3a,#123d20)" role="img" aria-label="Venice carnival masks">Venice Carnival<b>£599<small>PP</small></b></div>
<div class="abs offer" style="top:1587px;background:linear-gradient(160deg,#1f3a7a,#0e1c44)" role="img" aria-label="Easter Island statues">Easter Island<b>£2,999<small>PP</small></b></div>
<div class="abs offer" style="top:1737px;background:linear-gradient(160deg,#3a3a3a,#141414)" role="img" aria-label="Day of the Dead parade">Day of the Dead<b>£3,299<small>PP</small></b></div>

<div class="abs rule" style="top:1926px"></div>

<h2 class="abs h-section" style="left:0;top:1968px;width:1200px;text-align:center">Our Events</h2>
<article class="abs event" style="left:112px">
  <span class="date">26 JULY 2017 &nbsp;|&nbsp; MAXICO</span>
  <h3>Lumen lorem ipsum dolor sit dosis odio mauris.</h3>
  <p>Morbi accumsan ipsum velit. Nam nec used tellus a odio tincidunt auctor a ornare odio. Sed non mauris vitae erat consequat dosis auctor eu in elit. Class aptent taciti asumed sociosqu ad litora torquent per conubia era nostra, per inceptos himenaeos.</p>
  <div class="more">Readmore ▸</div>
</article>
<article class="abs event" style="left:446px">
  <span class="date">26 JULY 2017 &nbsp;|&nbsp; MAXICO</span>
  <h3>Lumen lorem ipsum dolor sit dosis odio mauris.</h3>
  <p>Morbi accumsan ipsum velit. Nam nec used tellus a odio tincidunt auctor a ornare odio. Sed non mauris vitae erat consequat dosis auctor eu in elit. Class aptent taciti asumed sociosqu ad litora torquent per conubia era nostra, per inceptos himenaeos.</p>
  <div class="more">Readmore ▸</div>
</article>
<article class="abs event" style="left:781px">
  <span class="date">26 JULY 2017 &nbsp;|&nbsp; MAXICO</span>
  <h3>Lumen lorem ipsum dolor sit dosis odio mauris.</h3>
  <p>Morbi accumsan ipsum velit. Nam nec used tellus a odio tincidunt auctor a ornare odio. Sed non mauris vitae erat consequat dosis auctor eu in elit. Class aptent taciti asumed sociosqu ad litora torquent per conubia era nostra, per inceptos himenaeos.</p>
  <div class="more">Readmore ▸</div>
</article>

<div class="abs rule" style="top:2372px"></div>

<div class="abs count">+300,000</div>
<div class="abs count-text">Happy customer<br>had to say about our<br>services</div>
<p class="abs quote">Morbi accumsan ipsum velit. Nam nec tellus a odio tincidunt auctor a ornare odio. Sed non mauris vitae erat consequat auctor eu in elit. Class aptent taciti sociosqu ad litora torquent per conubia nostra, per inceptos himenaeos. Mauris in erat justo. Nullam ac urna eu felis dapibus condimentum sit amet a augue. Sed non neque elit. Sed ut imperdiet nisi. Proin condimentum fermentum nunc. Etiam pharetra, erat sed aliquam massa nisl quis neque. Suspendisse in orci enim.</p>
<div class="abs quote-foot">
  <div class="sign" role="img" aria-label="Handwritten signature"></div>
  <div class="person"><b>MARA LINDEN</b>Lorem ipsum sit</div>
</div>
<div class="abs portrait" role="img" aria-label="Portrait of a smiling customer"></div>
<div class="abs dots"><span></span><span></span><span></span><span></span></div>

<footer class="abs site-footer"></footer>
<div class="abs partner" style="left:262px"></div>
<div class="abs partner" style="left:432px"></div>
<div class="abs partner" style="left:602px"></div>
<div class="abs partner" style="left:772px"></div>
<div class="abs footer-rule"></div>
<div class="abs f-col" style="left:112px">About us<br>Our Partners<br>Newsletter<br>FAQs</div>
<div class="abs f-col" style="left:261px">Contact Us<br>Booking Conditions<br>Privacy &amp; Cookies<br>Terms of Use</div>
<div class="abs f-col" style="left:454px">Financial Protection<br>Travel Insurance<br>Visas<br>Travel Advise</div>
<div class="abs f-col" style="left:643px">Group Booking<br>Tailor-Made &amp; Extra Nights<br>Booking Flights<br>Careers with LG</div>
<div class="abs f-col" style="left:863px;line-height:17px">LG Protecting Wildlife &amp; Animals and<br>supporting local communities<br><span style="display:block;margin-top:12px">Press Room</span></div>
<div class="abs social footer-social"><span></span><span></span><span></span><span></span><span></span></div>
<div class="abs copyright">Copyright © 2017 Lumen Getaways. All Rights Reserved</div>

</body>
</html>
```